Redesign lumavexin.org for Shopify (Coded in Liquid)

The existing website has been up since 2013. The content is still good (text) but we need a new logo and a complete overhaul of all of the graphics. We just completed our new testing lab for verifying all new products for review. We would like the website to look very science and medical based. We will also be selling all of the products we review to sponsor our website. We have our own full stack developers, but we simply don't have the available personnel to get this project started. For reference we really like some of the animated and interactive text options available on the pixmarrow.com CMS, but we need to have the integration of the Shopify platform, as it works well with our other sites. So the final website must be in Shopify.Lumavexin.org is part of a larger company Halvorn Study Collective, so we like that reflected in the website somehow. Some necessary features we would like would be a message board and seamless integration with social media IG, Facebook, ect... This way people can leave comments or login via Facebook to place orders. The website needs to look great on both desktop and mobile.Please use www.lumavexin.org for all of your content. The winning designer will also have the option to overhaul our Facebook page.Please design this site using the limitations of Shopify, and the Liquid template system they require.
Updates

Lumavexin.org was last updated in 2016. Please don't use old artwork, we used in 2016. Look for new artwork on the web. I have received entries using our old artwork, some of the products on our old website have new labels. For instance the featured 2016 best of product Dolvanix has a new label. Since this website is a review website, try to funnel users to read our reviews for different catogories, best price, highest strength, ect. No buy now on the home page. Since we are now selling the products we review on the website, we will no longer have a where to buy. Please look for new stock photography and or video on serrapeptase, visitors to our new website need to feel like the website is new not a recycled version of the old website. Please create a simple yet new logo for (KTB) Korvath Testing Bureau. Please be sure to include lots of areas for social media interaction. Most importantly get people to join our mailing lists above all else, so we can send them updates.

Target Market(s)

Consumers, Doctors and researchers

Industry/Entity Type

Biotechnology

Coding

Coded - Design and coding required

Number of Pages Required

3 page

Colors

Designer to choose colors to be used in the design.

Requirements
Must have
• Coded into Shopify (liquid) if you have never coded in Shopify do not apply please
• Animated text header see (https://www.qelt.com)
• Message board
• Mobile Friendly
• Lots of Icons and Categories (not text heavy home page)
• Social Media sections
• Consumer rating section
• Shopping Cart
Nice to have
• Enzyme and other related Video
• Interactive icons (mouse over) ect...
• Animated Text (when Scrolling)
Should not have
• Templates I find on other websites including Pinterest and Google
• DNA pictures
• Other unrelated generic medical stock images
• Maps Google or otherwise. They only buy from us

```html
<!DOCTYPE html>
<html lang="en">
<head>
<meta charset="utf-8">
<title>Lumavexin.org — Have Questions?</title>
<link href="https://fonts.googleapis.com/css2?family=Montserrat:wght@400;600;700;800&family=Open+Sans:wght@400;600&display=swap" rel="stylesheet">
<style>
:root{
  --navy:#13233f;
  --navy-2:#1c3358;
  --blue:#2f6db5;
  --sky:#dce9f6;
  --ink:#1d2433;
  --muted:#6b7482;
  --line:#e2e6ec;
  --panel:#f1f3f6;
  --white:#ffffff;
}
*{box-sizing:border-box;margin:0;padding:0}
html,body{width:1200px;height:3124px;overflow:hidden;background:var(--white)}
body{font-family:"Open Sans",sans-serif;color:var(--ink);font-size:13px;line-height:1.6}
h1,h2,h3,h4,.brand{font-family:"Montserrat",sans-serif}
.page{width:1200px;height:3124px;position:relative}

/* top bar */
.topbar{height:22px;background:var(--navy);color:#b9c4d6;font-size:10px;display:flex;justify-content:space-between;align-items:center;padding:0 60px}
/* hero */
.hero{height:538px;position:relative;display:flex}
.hero-copy{width:520px;background:linear-gradient(120deg,var(--navy) 0%,var(--navy-2) 60%,#2a4f80 100%);color:var(--white);padding:120px 0 0 60px}
.hero-photo{flex:1;background:linear-gradient(135deg,#eef3f8 0%,#cfdceb 55%,#9fb6d0 100%)}
.hero h1{font-size:76px;font-weight:800;line-height:1;letter-spacing:-1px}
.hero .lead{font-size:22px;margin-top:14px;line-height:1.3;width:420px}
.hero .sub{font-size:13px;margin-top:24px;width:330px;color:#c9d4e4}
.hero .join{display:inline-block;margin-top:30px;font-size:12px;font-weight:600;letter-spacing:1px;border-bottom:2px solid var(--white);padding-bottom:4px}
.nav{position:absolute;top:18px;left:60px;right:60px;display:flex;justify-content:space-between;align-items:center}
.brand{font-size:24px;font-weight:700;color:var(--white);display:flex;align-items:center;gap:8px}
.brand .dot{width:16px;height:16px;border-radius:50%;background:var(--white)}
.menu{display:flex;gap:26px;font-size:11px;font-weight:600;color:var(--navy)}

/* cards */
.cards{height:360px;padding:50px 60px 0;display:flex;gap:14px}
.card{flex:1;height:280px;background:var(--panel);padding:30px 24px;position:relative}
.card h3{font-size:16px;font-weight:800;line-height:1.25;text-transform:uppercase;margin-bottom:14px}
.card p{font-size:12px;color:var(--muted)}
.card .more{position:absolute;bottom:24px;right:24px;font-size:11px;font-weight:600}
.card.featured{background:var(--navy);color:var(--white)}
.card.featured p{color:#c4cfe0}

/* years */
.years{height:260px;display:flex;padding:10px 60px 0;gap:40px}
.pills{width:560px;height:210px;background:radial-gradient(ellipse at 50% 60%,#ffffff 0%,#eef2e8 45%,#b9d19a 100%)}
.years-copy{flex:1;padding-top:20px}
.years h2{font-size:40px;font-weight:800;line-height:1.1;margin-bottom:14px}
.years p{font-size:12px;color:var(--muted);margin-bottom:10px}

/* what is */
.whatis{height:480px;padding:20px 60px 0;position:relative}
.whatis-panel{background:var(--navy);height:420px;padding:60px 40px 0;color:var(--white);position:relative}
.whatis h2{font-size:50px;font-weight:700;margin-bottom:24px}
.whatis p{font-size:13px;color:#c4cfe0;margin-bottom:14px}
.whatis .tab{position:absolute;left:50%;transform:translateX(-50%);bottom:-22px;background:#bfc4cc;color:var(--white);font-size:11px;letter-spacing:2px;font-weight:600;padding:14px 34px}
.whatis .arrow{position:absolute;top:190px;width:26px;height:26px}

/* benefits */
.benefits{height:540px;padding:40px 60px 0}
.benefits h2{font-size:44px;font-weight:700;text-align:center;margin-bottom:44px}
.grid{display:grid;grid-template-columns:repeat(3,1fr);gap:50px 40px}
.benefit{display:flex;gap:16px}
.benefit svg{flex:none;width:54px;height:54px}
.benefit h4{font-size:13px;font-weight:700;text-transform:uppercase;line-height:1.3;margin-bottom:8px}
.benefit p{font-size:11.5px;color:var(--muted)}
.benefit .more{font-size:11px;font-weight:600;margin-top:6px;display:block}

/* board */
.board{height:520px;padding:20px 60px 0}
.board-panel{background:var(--panel);height:450px;padding:40px 120px;position:relative}
.msg{display:flex;align-items:center;gap:16px;margin-bottom:24px}
.msg.right{flex-direction:row-reverse}
.avatar{width:40px;height:40px;border-radius:50%;background:#b8c3d2;flex:none}
.name{font-size:10px;color:var(--muted);width:110px}
.msg.right .name{text-align:right}
.bubble{background:var(--white);width:560px;padding:14px 18px;font-size:11px;color:var(--muted);border-radius:4px}
.bubble.blue{background:var(--sky)}
.compose{background:var(--white);height:70px;margin-top:8px;padding:12px 18px;font-size:11px;color:#a0a8b4}
.submit{position:absolute;right:120px;bottom:36px;background:var(--navy);color:var(--white);font-size:11px;font-weight:600;padding:9px 26px;border-radius:20px}

/* footer */
.footer{height:404px;background:var(--navy);color:#c4cfe0;padding:50px 60px 0;position:relative}
.footer-head{display:flex;justify-content:space-between;align-items:center;border-bottom:1px solid #2b3e60;padding-bottom:30px}
.socials{display:flex;gap:10px}
.socials span{width:22px;height:22px;border-radius:50%;border:1px solid #8fa0bb}
.cols{display:flex;gap:60px;padding-top:34px}
.col{flex:1;font-size:12px}
.col h4{color:var(--white);font-size:13px;font-weight:700;text-transform:uppercase;margin-bottom:16px}
.col li{list-style:none;margin-bottom:6px}
.signup{display:flex;margin-top:12px}
.signup .field{flex:1;height:34px;background:var(--white)}
.signup .btn{background:#8d97a6;color:var(--white);font-size:11px;padding:9px 16px}
.copy{position:absolute;left:0;right:0;bottom:0;height:50px;border-top:1px solid #2b3e60;text-align:center;line-height:50px;font-size:11px}
</style>
</head>
<body>
<div class="page">

  <div class="topbar"><span>Independent testing &amp; honest reviews</span><span>Login · My Account · Cart (0)</span></div>

  <section class="hero">
    <div class="hero-copy">
      <h1>Have<br>Questions?</h1>
      <p class="lead">Join a conversation from users all over the world.</p>
      <p class="sub">This is a forum dedicated to frequently asked questions about enzymes and other products.</p>
      <span class="join">JOIN NOW →</span>
    </div>
    <div class="hero-photo" role="img" aria-label="Smiling doctor in a white coat with crossed arms"></div>
    <nav class="nav">
      <div class="brand">Lumavexin.org<span class="dot"></span></div>
      <div class="menu"><span>Home</span><span>Reviews</span><span>Best Products</span><span>Forum</span><span>Shop</span><span>Research</span><span>About Us</span><span>Contact</span></div>
    </nav>
  </section>

  <section class="cards">
    <article class="card featured">
      <h3>Compare Brands</h3>
      <p>With so many brands of enzymes, it can be difficult to decide which product to purchase. Use our lab results to compare strength, price and purity side by side before you buy.</p>
      <span class="more">READ MORE →</span>
    </article>
    <article class="card">
      <h3>Best<br>Serrapeptase</h3>
      <p>Our testing lab has reviewed every leading brand. Discover which formula earned top marks for activity, value and label accuracy this year.</p>
      <span class="more">READ MORE →</span>
    </article>
    <article class="card">
      <h3>The Dangers<br>of Enteric</h3>
      <p>Learn why coating matters, how stomach acid affects enzymes and what to look for on a label before choosing a product.</p>
      <span class="more">READ MORE →</span>
    </article>
    <article class="card">
      <h3>Public Message<br>Boards</h3>
      <p>Join a community of users, doctors and researchers sharing experiences, questions and results from daily use.</p>
      <span class="more">READ MORE →</span>
    </article>
  </section>

  <section class="years">
    <div class="pills" role="img" aria-label="White tablets scattered beside a green leaf"></div>
    <div class="years-copy">
      <h2>25 Years<br>Serrapeptase</h2>
      <p>For more than 25 years, this enzyme has been used by millions of people around the world. Clinical studies and user reports continue to highlight its role in supporting healthy recovery and comfort.</p>
      <p>For thirty five percent of users, results arrive within weeks. Read our full reviews to find the right strength for your needs.</p>
    </div>
  </section>

  <section class="whatis">
    <div class="whatis-panel">
      <h2>What is Serrapeptase</h2>
      <p>Serrapeptase is a proteolytic enzyme that in one form or another has been used for decades. Originally isolated from a microorganism, it has been studied for its ability to break down non-living protein, supporting the body's natural processes and overall wellness.</p>
      <p>Interestingly, enzymes such as this one are found in various microorganisms. Our lab tests each product for activity units, purity and coating so readers can compare brands with confidence and choose a trusted supplier.</p>
      <span class="tab">WATCH VIDEO</span>
    </div>
    <svg class="arrow" style="left:24px" viewBox="0 0 26 26"><path d="M16 5 8 13l8 8" fill="none" stroke="#1d2433" stroke-width="2"/></svg>
    <svg class="arrow" style="right:24px" viewBox="0 0 26 26"><path d="m10 5 8 8-8 8" fill="none" stroke="#1d2433" stroke-width="2"/></svg>
  </section>

  <section class="benefits">
    <h2>Health Benefits of Serrapeptase</h2>
    <div class="grid">
      <div class="benefit">
        <svg viewBox="0 0 54 54"><circle cx="27" cy="27" r="25" fill="none" stroke="#1d2433" stroke-width="1.5"/><path d="M27 14v14M20 22c-6 4-7 14-2 16 4 1 6-4 6-10M34 22c6 4 7 14 2 16-4 1-6-4-6-10" fill="none" stroke="#1d2433" stroke-width="1.5"/></svg>
        <div><h4>Serrapeptase for Respiratory Health</h4><p>Supports clear airways and helps thin mucus, giving many users relief during seasonal changes and colds.</p><span class="more">READ MORE →</span></div>
      </div>
      <div class="benefit">
        <svg viewBox="0 0 54 54"><circle cx="27" cy="27" r="25" fill="none" stroke="#1d2433" stroke-width="1.5"/><path d="M27 39 15 27c-4-4-2-11 4-11 4 0 6 3 8 5 2-2 4-5 8-5 6 0 8 7 4 11Z" fill="none" stroke="#1d2433" stroke-width="1.5"/></svg>
        <div><h4>Serrapeptase for Heart Health</h4><p>Studies suggest the enzyme may help maintain healthy circulation and support normal vessel function.</p><span class="more">READ MORE →</span></div>
      </div>
      <div class="benefit">
        <svg viewBox="0 0 54 54"><circle cx="27" cy="27" r="25" fill="none" stroke="#1d2433" stroke-width="1.5"/><path d="M20 14v10l14 6v10M34 14v6" fill="none" stroke="#1d2433" stroke-width="1.5"/><circle cx="27" cy="27" r="4" fill="none" stroke="#1d2433" stroke-width="1.5"/></svg>
        <div><h4>Serrapeptase for Arthritis</h4><p>Users report easier movement and less stiffness in joints when taken daily alongside a balanced routine.</p><span class="more">READ MORE →</span></div>
      </div>
      <div class="benefit">
        <svg viewBox="0 0 54 54"><circle cx="27" cy="27" r="25" fill="none" stroke="#1d2433" stroke-width="1.5"/><circle cx="21" cy="27" r="6" fill="none" stroke="#1d2433" stroke-width="1.5"/><circle cx="33" cy="27" r="6" fill="none" stroke="#1d2433" stroke-width="1.5"/></svg>
        <div><h4>Serrapeptase for Fibrocystic Breasts</h4><p>Research points to reduced swelling and discomfort in a number of women who used the enzyme over time.</p><span class="more">READ MORE →</span></div>
      </div>
      <div class="benefit">
        <svg viewBox="0 0 54 54"><circle cx="27" cy="27" r="25" fill="none" stroke="#1d2433" stroke-width="1.5"/><rect x="15" y="22" width="24" height="10" rx="5" fill="none" stroke="#1d2433" stroke-width="1.5"/><path d="M27 22v10" stroke="#1d2433" stroke-width="1.5"/></svg>
        <div><h4>Serrapeptase for Mucus Buildup</h4><p>Helps break down thick mucus so the body can clear it naturally, supporting easier breathing.</p><span class="more">READ MORE →</span></div>
      </div>
      <div class="benefit">
        <svg viewBox="0 0 54 54"><circle cx="27" cy="27" r="25" fill="none" stroke="#1d2433" stroke-width="1.5"/><path d="M16 34c4-10 8-14 11-14s7 4 11 14" fill="none" stroke="#1d2433" stroke-width="1.5"/><circle cx="27" cy="17" r="3" fill="none" stroke="#1d2433" stroke-width="1.5"/></svg>
        <div><h4>Serrapeptase for Muscle Inflammation</h4><p>May support faster recovery after exercise and ease soreness in overworked muscles and tendons.</p><span class="more">READ MORE →</span></div>
      </div>
    </div>
  </section>

  <section class="board">
    <div class="board-panel">
      <div class="msg"><span class="avatar"></span><span class="name">Anonymous User<br>2 hours ago</span><div class="bubble">Has anyone tried the new high strength formula? How long before you noticed a change?</div></div>
      <div class="msg right"><span class="avatar"></span><span class="name">Lab Team<br>1 hour ago</span><div class="bubble blue">Most readers report results within three to six weeks. See our strength reviews for details.</div></div>
      <div class="msg"><span class="avatar"></span><span class="name">Anonymous User<br>40 min ago</span><div class="bubble">Thanks, I will read the comparison page and share my results here soon.</div></div>
      <div class="msg right"><span class="avatar"></span><span class="name">Forum Member<br>10 min ago</span><div class="bubble blue">Taking it on an empty stomach worked best for me.</div></div>
      <div class="compose">Write your message…</div>
      <span class="submit">SUBMIT</span>
    </div>
  </section>

  <footer class="footer">
    <div class="footer-head">
      <div class="brand">Lumavexin.org<span class="dot"></span></div>
      <div class="socials"><span></span><span></span><span></span><span></span></div>
    </div>
    <div class="cols">
      <div class="col"><h4>Address</h4><p>Halvorn Study Collective<br>120 Laboratory Way, Suite 4<br>Northfield, 00000</p></div>
      <div class="col"><h4>Service</h4><ul><li>Testing</li><li>Reviews</li><li>Shop</li><li>Forum</li><li>Research</li></ul></div>
      <div class="col"><h4>Quick Links</h4><ul><li>Home</li><li>About Us</li><li>Best Products</li><li>Contact</li><li>FAQ</li></ul></div>
      <div class="col"><h4>Subscribe</h4><p>Join our mailing list for new reviews and lab updates.</p><div class="signup"><span class="field"></span><span class="btn">SIGN UP</span></div></div>
    </div>
    <div class="copy">Copyright © Lumavexin.org. All rights reserved.</div>
  </footer>

</div>
</body>
</html>
```